Website Redesign using existing images, copy etc.

I'm looking for a website redesign/refresh of my current WordPress website. I would like to utilize the same photography, a new photo viewer, and an overall refresh of the entire design. This will need to be WordPress with simple accessibility to make changes as we add additional properties and make updates. We auction luxury real estate and luxury yachts for non-distressed sellers. It needs to be simple, luxurious and with ease of use for both web and especially mobile. www.MarlowenGroup.com

```html
<!DOCTYPE html>
<html lang="en">
<head>
<meta charset="utf-8">
<title>Marlowen Auctions — Real Estate &amp; Yachts</title>
<link rel="stylesheet" href="https://fonts.googleapis.com/css2?family=Crimson+Text:wght@400;600&family=Montserrat:wght@400;500;600&display=swap">
<style>
:root{
  --gold:#9a835d;
  --gold-light:#b39d77;
  --beige:#cdc3ae;
  --beige-soft:#d9d1c1;
  --card-brown:#948564;
  --footer-brown:#857559;
  --bar:#c9bfa9;
  --panel-grey:#efeeea;
  --text:#2b2a28;
  --white:#ffffff;
}
*{margin:0;padding:0;box-sizing:border-box}
html,body{width:1200px;height:2716px;overflow:hidden;background:var(--white)}
body{position:relative;font-family:"Montserrat",sans-serif;color:var(--text)}
.serif{font-family:"Crimson Text",serif;font-weight:400}
.abs{position:absolute}

/* hero */
.hero{left:0;top:0;width:1200px;height:580px;overflow:hidden}
.hero-photo{position:absolute;inset:0;
  background:
    radial-gradient(ellipse 180px 140px at 1080px 300px,rgba(214,150,70,.55),rgba(214,150,70,0) 70%),
    radial-gradient(ellipse 260px 160px at 640px 270px,rgba(180,120,70,.35),rgba(180,120,70,0) 70%),
    radial-gradient(ellipse 520px 220px at 600px 250px,rgba(190,178,160,.45),rgba(190,178,160,0) 75%),
    radial-gradient(ellipse 240px 120px at 920px 280px,rgba(160,40,70,.35),rgba(160,40,70,0) 70%),
    linear-gradient(180deg,#2e2f36 0%,#3a3b42 22%,#4c4a46 42%,#4f5040 62%,#3a4430 80%,#2c3326 100%)}
.hero-curve{position:absolute;left:0;top:0}
.brand-mark{left:88px;top:17px;width:46px;height:46px;border:1.5px solid var(--beige);border-radius:50%}
.nav{right:88px;top:36px;display:flex;gap:26px;align-items:center;font-size:14px;color:var(--white);letter-spacing:.3px}
.nav a{color:var(--white);text-decoration:none}
.nav .active{text-decoration:underline;color:var(--beige)}
.nav .phone{display:flex;align-items:center;gap:6px}
.hero-title{left:0;width:1200px;top:184px;display:flex;justify-content:center;align-items:center;gap:24px;color:var(--white);font-size:46px;letter-spacing:14px}
.hero-title .ring{width:76px;height:76px;border:3px solid var(--white);border-radius:50%}
.hero-sub{left:0;width:1200px;top:276px;text-align:center;color:var(--white);font-size:16px;letter-spacing:4px;font-weight:500}
.btn{display:inline-flex;align-items:center;justify-content:center;border-radius:20px;font-weight:600;font-size:12px;letter-spacing:.5px;color:var(--text);text-decoration:none}
.hero-btns{left:0;width:1200px;top:333px;display:flex;justify-content:center;gap:9px}
.hero-btns .btn{width:270px;height:36px}
.btn-light{background:var(--beige-soft)}
.btn-gold{background:var(--gold-light);color:var(--white)}

/* intro */
.icon-ring{width:36px;height:36px;border:1.5px solid var(--beige);border-radius:50%}
.intro-icon{left:582px;top:660px}
.intro-title{left:0;width:1200px;top:704px;text-align:center;color:var(--gold);font-size:22px}
.intro-sub{left:0;width:1200px;top:734px;text-align:center;color:var(--gold);font-size:15px}
.intro-text{left:170px;width:860px;top:772px;text-align:center;font-size:13.5px;line-height:24px}

/* featured */
.press-panel{left:0;top:935px;width:362px;height:427px;background:var(--panel-grey)}
.press-list{left:145px;top:985px;width:165px;display:flex;flex-direction:column;align-items:center;gap:30px;color:#8f8d89}
.press-list span{font-family:"Crimson Text",serif;font-size:22px;font-weight:600;text-align:center;line-height:24px}
.villa{
  background:
    radial-gradient(ellipse 130px 90px at 28% 12%,rgba(240,170,150,.55),rgba(240,170,150,0) 70%),
    radial-gradient(ellipse 34% 26% at 50% 48%,rgba(232,196,176,.85),rgba(232,196,176,0) 75%),
    radial-gradient(ellipse 18% 14% at 32% 30%,rgba(170,110,110,.7),rgba(170,110,110,0) 75%),
    radial-gradient(ellipse 18% 14% at 66% 34%,rgba(170,110,110,.6),rgba(170,110,110,0) 75%),
    radial-gradient(ellipse 30% 40% at 5% 70%,rgba(46,64,34,.9),rgba(46,64,34,0) 75%),
    radial-gradient(ellipse 30% 40% at 96% 72%,rgba(46,64,34,.9),rgba(46,64,34,0) 75%),
    linear-gradient(180deg,#c9a7a0 0%,#b89a97 10%,#7b7266 18%,#a68a80 40%,#8a7868 60%,#4b5534 82%,#33402a 100%)}
.featured-photo{left:652px;top:935px;width:548px;height:427px}
.featured-card{left:362px;top:916px;width:290px;height:469px;background:var(--card-brown);border-radius:12px;color:var(--white);text-align:center}
.featured-card .icon-ring{position:absolute;left:127px;top:62px;border-color:var(--beige)}
.featured-card h2{position:absolute;top:110px;width:100%;font-family:"Crimson Text",serif;font-weight:400;font-size:22px}
.featured-card p{position:absolute;top:148px;left:38px;width:214px;font-size:13.5px;line-height:22.5px}
.featured-card .btn{position:absolute;left:79px;top:373px;width:133px;height:36px;background:var(--beige-soft)}

/* sold */
.sold-icon{left:582px;top:1474px}
.sold-title{left:0;width:1200px;top:1513px;text-align:center;color:var(--gold);font-size:22px}
.slide{top:1563px;height:427px;border-radius:14px;border:2px solid var(--beige-soft);overflow:hidden}
.slide-main{left:158px;width:884px}
.slide-peek{width:142px;background:linear-gradient(180deg,#e8e7e3,#dedcd6 60%,#d8d7d0)}
.caption{left:448px;top:1939px;width:305px;height:101px;background:var(--white);border-radius:10px;box-shadow:0 4px 14px rgba(0,0,0,.12);text-align:center}
.caption .place{margin-top:16px;color:var(--gold);font-size:20px}
.caption .btn{margin-top:10px;width:161px;height:35px;background:var(--beige)}
.dots{left:0;width:1200px;top:2066px;display:flex;justify-content:center;gap:6px}
.dots i{width:13px;height:13px;border:1.3px solid var(--gold-light);border-radius:50%}
.dots i.on{background:var(--gold)}
.sold-text{left:190px;width:820px;top:2110px;text-align:center;font-size:13.5px;line-height:21px}

/* footer */
.footer-curve{left:0;top:2360px}
.footer-brand{left:0;width:1200px;top:2458px;display:flex;justify-content:center;align-items:center;gap:22px;color:var(--white);font-size:32px;letter-spacing:10px}
.footer-brand .ring{width:56px;height:56px;border:2.5px solid var(--white);border-radius:50%}
.badge{left:126px;top:2554px;width:50px;height:50px;border:3px solid var(--beige-soft);border-radius:50%}
.foot-nav{top:2551px;display:flex;flex-direction:column;gap:9px;font-size:14px;color:var(--white)}
.foot-nav .active{color:var(--beige);text-decoration:underline}
.alerts-label{left:465px;top:2552px;color:var(--beige);font-weight:600;font-size:13.5px}
.field{top:2580px;height:38px;border:1.3px solid var(--beige);border-radius:19px;color:var(--beige);font-size:13.5px;padding-left:23px;display:flex;align-items:center}
.submit{left:958px;top:2580px;width:119px;height:38px;background:var(--beige-soft);font-size:14px;font-weight:500}
.bottom-bar{left:0;top:2676px;width:1200px;height:40px;background:var(--bar);display:flex;align-items:center;padding-left:88px;font-size:14px;color:#3c3a36;gap:17px}
.socials{right:86px;top:2686px;display:flex;gap:13px}
.socials i{width:20px;height:20px;border-radius:50%;background:#4d4a44}
</style>
</head>
<body>

<header class="hero abs">
  <div class="hero-photo" role="img" aria-label="Dusk view of a Spanish-style estate with white chimneys, a wooden pergola, lit windows and a terraced garden"></div>
  <svg class="hero-curve" width="1200" height="580" viewBox="0 0 1200 580" aria-hidden="true">
    <path d="M0 448 C 300 560, 900 570, 1200 448 L1200 580 L0 580 Z" fill="#b9aa8b"/>
    <path d="M0 478 C 320 590, 880 585, 1200 470 L1200 580 L0 580 Z" fill="#ddd5c5"/>
    <path d="M0 492 C 320 600, 880 592, 1200 482 L1200 580 L0 580 Z" fill="#c9bea7"/>
    <path d="M0 520 C 350 620, 880 600, 1200 505 L1200 580 L0 580 Z" fill="#ffffff"/>
  </svg>
</header>

<div class="brand-mark abs" aria-label="Marlowen Auctions"></div>
<nav class="nav abs">
  <a class="active" href="#">BUY</a><a href="#">SELL</a><a href="#">ABOUT</a><a href="#">CONTACT</a>
  <span class="phone"><svg width="12" height="12" viewBox="0 0 24 24" aria-hidden="true"><path fill="#fff" d="M6.6 10.8a15 15 0 006.6 6.6l2.2-2.2a1 1 0 011-.2 11 11 0 003.6.6 1 1 0 011 1V20a1 1 0 01-1 1A17 17 0 013 4a1 1 0 011-1h3.5a1 1 0 011 1 11 11 0 00.6 3.6 1 1 0 01-.2 1z"/></svg>800-555-0148</span>
</nav>

<h1 class="hero-title abs serif"><span>MARLOWEN</span><span class="ring"></span><span>AUCTIONS</span></h1>
<div class="hero-sub abs">Real Estate &amp; Yachts</div>
<div class="hero-btns abs">
  <a class="btn btn-light" href="#">BROWSE UPCOMING AUCTIONS</a>
  <a class="btn btn-gold" href="#">BROWSE PAST SUCCESSES</a>
</div>

<section>
  <div class="icon-ring intro-icon abs"></div>
  <h2 class="intro-title abs serif">Over One Billion Dollars of Auctions Marketed</h2>
  <div class="intro-sub abs">Real Estate &amp; Yachts</div>
  <p class="intro-text abs">The experience of hearing the auctioneer’s final proclamation of “SOLD!” is unparalleled. Whether it’s the initial meeting with the seller at their estate or yacht, or the triumphant raising of the paddle by the winning buyer, we relish every moment of the process and the ensuing festivities. We’re confident that you will, too.</p>
</section>

<section>
  <div class="press-panel abs"></div>
  <div class="press-list abs">
    <span>The Daily Ledger</span>
    <span>Capital Weekly</span>
    <span>Estate Review</span>
    <span>Market Channel</span>
    <span>News Network</span>
  </div>
  <div class="featured-photo villa abs" role="img" aria-label="Aerial sunset view of a waterfront Mediterranean villa with domed towers among palms"></div>
  <div class="featured-card abs">
    <div class="icon-ring"></div>
    <h2>As Featured In</h2>
    <p>By offering top-tier properties and vessels globally, along with strategic auction dates, excep-tional marketing tactics, and a diligent public relations team, even the most prominent media outlets have taken notice. Check out some of our latest press features.</p>
    <a class="btn" href="#">View Press</a>
  </div>
</section>

<section>
  <div class="icon-ring sold-icon abs"></div>
  <h2 class="sold-title abs serif">Sold by Marlowen Auctions</h2>
  <div class="slide slide-peek abs" style="left:-2px" role="img" aria-label="Faded preview of previous sold property"></div>
  <div class="slide slide-main villa abs" role="img" aria-label="Aerial sunset view of a sold waterfront villa in Frisco, Texas"></div>
  <div class="slide slide-peek abs" style="left:1060px" role="img" aria-label="Faded preview of next sold property"></div>
  <div class="caption abs">
    <div class="place serif">Frisco | Texas</div>
    <a class="btn" href="#">SUCCESS STORY</a>
  </div>
  <div class="dots abs"><i></i><i></i><i></i><i></i><i></i><i class="on"></i><i></i></div>
  <p class="sold-text abs">Marlowen Auctions is a top-tier destination for luxury property auctions, having overseen the auction marketing of numerous high-end estates and yachts. Our team of luxury home auction experts is committed to helping property owners obtain the best value for their assets while ensuring a timely sale. Whether you have an expansive compound or a metropolitan penthouse, Marlowen Auctions has the necessary skills and expertise to facilitate various luxury real estate auctions. What’s even better? Our team takes care of every aspect of the process in cooperation with tour realtor/broker, including property tours, photography and cinematography, marketing advertising, public relations and more. Apart from high-end real estate auctions, we can also organize and execute luxury yacht auctions to help boat owners find qualified buyers for their vessels. Interested in finding out more about our luxury home and yacht auctions? Explore our current listings and success stories!</p>
</section>

<footer>
  <svg class="footer-curve abs" width="1200" height="316" viewBox="0 0 1200 316" aria-hidden="true">
    <path d="M0 70 C 300 -10, 850 -10, 1200 60 L1200 316 L0 316 Z" fill="#ddd5c5"/>
    <path d="M0 75 C 350 5, 900 10, 1200 90 L1200 316 L0 316 Z" fill="#cdc3ae"/>
    <path d="M0 60 C 350 10, 850 20, 1200 140 L1200 316 L0 316 Z" fill="#857559"/>
  </svg>
  <div class="footer-brand abs serif"><span>MARLOWEN</span><span class="ring"></span><span>AUCTIONS</span></div>
  <div class="badge abs" role="img" aria-label="Veteran owned business badge"></div>
  <div class="foot-nav abs" style="left:253px"><span class="active">HOME</span><span>BUY</span><span>SELL</span></div>
  <div class="foot-nav abs" style="left:337px"><span>ABOUT</span><span>BLOG</span><span>CONTACT</span></div>
  <div class="alerts-label abs">SIGN UP FOR MARLOWEN ALERTS</div>
  <div class="field abs" style="left:465px;width:239px">Name</div>
  <div class="field abs" style="left:712px;width:238px">Email</div>
  <a class="btn submit abs" href="#">Submit</a>
  <div class="bottom-bar abs"><span>© 2023 Marlowen Auctions. All Right Reserved</span><span>|</span><span>Terms Of Service</span><span>Copyright Policy</span><span>Privacy Policy</span></div>
  <div class="socials abs" aria-label="Social links"><i></i><i></i><i></i><i></i></div>
</footer>

</body>
</html>
```